Accounting firm needing business card / letterhead designed
Marcus T. Elbering, CPA
marcus@fernquill.com
www.fernquill.com
482 N Harlow Ave Corwin Falls, OH 43719
419-555-0172

```html
<!DOCTYPE html>
<html lang="en">
<head>
<meta charset="utf-8">
<title>Fernquill Accounting – Business Card</title>
<link rel="stylesheet" href="https://fonts.googleapis.com/css2?family=Arimo:wght@400;700&display=swap">
<style>
  :root {
    --stage: #3a3a3c;
    --card-black: #000000;
    --band-grey: #d9d9d9;
    --stripe-grey: #4a4a4c;
    --lime: #8cc63f;
    --navy: #262378;
    --white: #ffffff;
  }
  * { margin: 0; padding: 0; box-sizing: border-box; }
  html, body {
    width: 1200px; height: 1000px; overflow: hidden;
    background: var(--stage);
    font-family: "Arimo", Arial, sans-serif;
  }
  .card {
    position: absolute;
    width: 700px; height: 400px;
    background: var(--card-black);
    overflow: hidden;
    box-shadow: 0 10px 30px rgba(0,0,0,.35);
  }
  .card--back { left: 80px; top: 60px; }
  .card--front { left: 420px; top: 530px; }

  /* back side */
  .brand-band {
    position: absolute; left: 250px; right: 0; top: 150px; height: 60px;
    background: var(--band-grey);
  }
  .brand-band__name {
    position: absolute; left: 28px; top: 8px;
    font-size: 44px; font-weight: 700; letter-spacing: 2px;
    color: var(--navy);
  }
  .accent-band {
    position: absolute; left: 250px; right: 0; top: 210px; height: 24px;
    background: var(--lime);
  }
  .website {
    position: absolute; left: 330px; top: 244px;
    font-size: 15px; letter-spacing: 1.5px; color: var(--white);
  }

  /* front side */
  .contact-panel {
    position: absolute; left: 460px; top: 0; right: 0; bottom: 0;
    background: var(--navy);
  }
  .social {
    position: absolute; right: 18px; top: 14px;
    display: flex; align-items: center; gap: 6px;
    font-size: 10px; color: var(--white);
  }
  .social__dot { width: 11px; height: 11px; border-radius: 50%; background: var(--white); }
  .front-brand {
    position: absolute; left: 95px; top: 62px;
    font-size: 48px; font-weight: 700; letter-spacing: 2px; color: var(--white);
  }
  .person {
    position: absolute; left: 130px; top: 168px;
    font-size: 22px; font-weight: 400; color: var(--white);
  }
  .row {
    position: absolute; left: 0; width: 700px; height: 28px;
  }
  .row__fill {
    position: absolute; top: 0; bottom: 0; right: 300px;
    background: var(--stripe-grey);
  }
  .row__value {
    position: absolute; right: 310px; top: 6px;
    font-size: 15px; line-height: 16px; color: var(--white); white-space: nowrap;
  }
  .row__label {
    position: absolute; left: 400px; right: 0; top: 0; bottom: 0;
    background: var(--lime);
    padding: 6px 0 0 14px;
    font-size: 14px; line-height: 16px; color: var(--navy);
  }
  .row--address { top: 226px; }
  .row--phone   { top: 258px; }
  .row--email   { top: 290px; }
  .row--address .row__fill { left: 90px; }
  .row--phone .row__fill { left: 40px; }
  .row--email .row__fill { left: 0; }

  .stripe {
    position: absolute; left: 0; width: 460px; height: 22px;
    background: var(--stripe-grey);
  }
  .stripe--one { top: 330px; }
  .stripe--two { top: 362px; }
</style>
</head>
<body>

<section class="card card--back" aria-label="Card back">
  <div class="brand-band"><span class="brand-band__name">FERNQUILL</span></div>
  <div class="accent-band"></div>
  <p class="website">www.fernquill.com</p>
</section>

<section class="card card--front" aria-label="Card front">
  <div class="contact-panel">
    <div class="social"><span class="social__dot"></span><span>Fernquill Accounting</span></div>
  </div>

  <p class="front-brand">FERNQUILL</p>
  <p class="person">Marcus T. Elbering, CPA</p>

  <div class="row row--address">
    <span class="row__fill"></span>
    <span class="row__value">482 N Harlow Ave Corwin Falls, OH 43719</span>
    <span class="row__label">Address</span>
  </div>
  <div class="row row--phone">
    <span class="row__fill"></span>
    <span class="row__value">419-555-0172</span>
    <span class="row__label">Phone</span>
  </div>
  <div class="row row--email">
    <span class="row__fill"></span>
    <span class="row__value">marcus@fernquill.com</span>
    <span class="row__label">Email</span>
  </div>

  <div class="stripe stripe--one"></div>
  <div class="stripe stripe--two"></div>
</section>

</body>
</html>
```